Business to Business Website Homepage Design

Hi, My Web Developer is giving me designs that aren't quite taking my fancy as far as visual impact. I'd love to see designs come out which are simple, fresh and powerful.
I just want a PDF document that I can give to my web developer to follow, so this project is NOT to make a website, its to design the homepage.
I would like it to scroll down through different areas of my website on the homepage. Our colours are Blood Orange, White, Grey & Black.
I like these websites:
Simplicity
https://www.quenvalo.com/au/webapps/mpp/home
Our Team Section
http://trelmicode.com.au/
We'd like our logo on top left. Nav bar top right. Have an image which we can place a headline subject on + video icon which will pop out with a video and opt in for name and email with a heading so people know what they're opting in for.
The next section should have a lot of white space, this "What we do" which is 1) Grow in size so your business can get bigger 2) increase in value, so you maximise what your business is worth 3) Free up your time, so you can live the lifestyle you've always wanted. Our brief was we want image/text combo with a lot of white space,
Then we have our services
After Services, would like to have a "Why Work With Us" section
Then a testimonials section
Then "Our Team"
Then contact us.
Thats pretty much it, we'd just love some different ideas, these guys are almost there, but just need more impact.
Updates
Target Market(s)
Business Owners between $1m to $3m turnover
Industry/Entity Type
Business
Number of Pages Required
1 page
Look and feel
Each slider illustrates characteristics of the customer's brand and the style your logo design should communicate.

```html
<!DOCTYPE html>
<html lang="en">
<head>
<meta charset="utf-8">
<title>Kestrel Union – Home</title>
<link href="https://fonts.googleapis.com/css2?family=Raleway:wght@300;400;500;600;700&family=Lato:ital,wght@0,400;1,400&display=swap" rel="stylesheet">
<style>
:root{
  --red:#c8312a;
  --red-soft:#e39a92;
  --black:#0b0b0b;
  --grey-bg:#f2f2f2;
  --text:#333;
  --muted:#8a8a8a;
  --white:#fff;
}
*{box-sizing:border-box;margin:0;padding:0}
html,body{width:1200px;height:2769px;overflow:hidden}
body{position:relative;background:var(--white);font-family:"Raleway",sans-serif;color:var(--text)}
.abs{position:absolute}

/* header */
.site-header{left:0;top:0;width:1200px;height:80px;background:var(--white);z-index:3}
.brand{left:150px;top:20px;display:flex;align-items:center;gap:10px}
.brand-dot{width:40px;height:40px;border-radius:50%;background:var(--red)}
.brand-name{font-weight:700;font-size:26px;color:var(--red);letter-spacing:1px}
.main-nav{left:520px;top:32px;display:flex;gap:22px;font-size:16px;color:#444}
.main-nav .active{color:var(--red);border-bottom:3px solid var(--red);padding-bottom:6px}

/* hero */
.hero{left:0;top:80px;width:1200px;height:473px;background:linear-gradient(135deg,#3b3d42 0%,#6b6560 40%,#8d7c70 60%,#4a4b50 100%)}
.hero-shade{left:0;top:80px;width:1200px;height:473px;background:linear-gradient(180deg,rgba(0,0,0,.15),rgba(0,0,0,.4))}
.side-tab{left:0;top:150px;width:168px;height:40px;background:var(--red);color:var(--white);font-size:17px;line-height:40px;padding-left:20px}
.side-btn{left:0;width:46px;height:40px;background:var(--red)}
.play{left:552px;top:237px}
.hero-title{left:0;top:436px;width:1200px;text-align:center;color:var(--white);font-weight:600;font-size:27px}
.optin{left:148px;top:517px;width:904px;height:86px;background:var(--white);box-shadow:0 3px 10px rgba(0,0,0,.18);border-radius:3px;z-index:5}
.optin-field{top:22px;height:42px;border:1.5px solid var(--red);font-family:"Lato",sans-serif;font-style:italic;font-size:14px;color:#aaa;text-align:center;line-height:39px}
.optin-btn{left:696px;top:22px;width:158px;height:42px;background:var(--red);color:var(--white);font-weight:700;font-size:17px;text-align:center;line-height:42px}

/* achievements */
.achieve{left:0;top:553px;width:1200px;height:517px;background:var(--grey-bg)}
.section-title{width:1200px;left:0;text-align:center;font-size:28px;font-weight:400;color:var(--red)}
.divider{left:520px;width:160px;height:10px}
.goal{width:300px;text-align:center}
.goal-icon{width:96px;height:96px;border-radius:50%;background:var(--white);margin:0 auto 22px;display:flex;align-items:center;justify-content:center}
.goal-title{font-size:18px;line-height:24px;color:#333}
.goal-text{margin-top:18px;font-family:"Lato",sans-serif;font-size:13.5px;line-height:20px;color:var(--muted)}
.goal.active .goal-icon{background:var(--red-soft)}
.goal.active .goal-title,.goal.active .goal-text{color:var(--red)}

/* services */
.service{width:300px;display:flex;gap:18px}
.service-icon{width:34px;height:28px;flex:none}
.service-name{font-size:19px;color:#333;margin-bottom:8px}
.service-text{font-family:"Lato",sans-serif;font-size:11.5px;line-height:16px;color:#444;width:230px}
.more{color:var(--red);font-weight:700;font-family:"Raleway",sans-serif}

/* why */
.why{left:0;top:1540px;width:1200px;height:282px;background:linear-gradient(120deg,#2f3237,#55575b 50%,#3c3e43)}
.why-title{left:0;top:1588px;width:1200px;text-align:center;color:var(--white);font-size:28px;font-weight:600}
.why-text{left:305px;top:1670px;width:590px;text-align:center;color:var(--white);font-size:19px;font-weight:500;line-height:29px}

/* team */
.team-tabs{left:150px;top:1897px;font-size:16px;color:#777;display:flex;gap:10px}
.team-tabs .on{color:var(--red);text-decoration:underline}
.team-dot{top:1912px;width:7px;height:7px;border-radius:50%;background:#bbb}
.member{width:200px;height:181px}
.member-hover{left:400px;top:1975px;width:200px;height:181px;background:rgba(40,40,40,.75);color:var(--white);text-align:center}
.member-name{margin-top:90px;font-weight:700;font-size:19px}
.member-social{display:flex;gap:10px;justify-content:center;margin-top:12px}
.soc{width:14px;height:14px;border-radius:50%;background:var(--white)}

/* testimonials & contact */
.quote-title{font-size:28px;font-weight:600;color:var(--white)}
.avatar{left:152px;top:2547px;width:96px;height:96px;border-radius:50%;border:4px solid var(--white);background:linear-gradient(135deg,#6b4a3a,#b08268)}
.quote-mark{color:var(--white);font-size:44px;font-weight:700;line-height:1}
.quote-text{left:318px;top:2555px;width:275px;color:var(--white);font-size:16px;font-weight:600;line-height:22px}
.slide-dot{top:2686px;width:7px;height:7px;border-radius:50%;background:rgba(255,255,255,.5)}
.contact-line{left:776px;display:flex;gap:12px;color:var(--white);font-size:17px;font-weight:600;line-height:24px}
.footer-copy{left:150px;top:2738px;color:var(--white);font-size:14px}
.footer-soc{top:2740px;width:18px;height:18px;border-radius:50%;background:var(--white)}
</style>
</head>
<body>

<header class="site-header abs">
  <div class="brand abs"><span class="brand-dot"></span><span class="brand-name">KESTREL UNION</span></div>
  <nav class="main-nav abs">
    <span class="active">HOME</span><span>ABOUT US</span><span>OUR SERVICES</span><span>OUR TEAM</span><span>CONTACT US</span>
  </nav>
</header>

<section>
  <div class="hero abs" role="img" aria-label="Photo of business people smiling in a meeting"></div>
  <div class="hero-shade abs"></div>
  <div class="side-tab abs">Your Business</div>
  <div class="side-btn abs" style="top:205px"><svg width="46" height="40"><circle cx="23" cy="20" r="10" fill="none" stroke="#fff" stroke-width="2"/><path d="M23 14v12M17 20h12" stroke="#fff" stroke-width="2"/></svg></div>
  <div class="side-btn abs" style="top:265px"><svg width="46" height="40"><circle cx="23" cy="20" r="10" fill="none" stroke="#fff" stroke-width="2"/><path d="M23 14v12M17 20h12" stroke="#fff" stroke-width="2"/></svg></div>
  <svg class="play abs" width="96" height="96" aria-label="Play video"><circle cx="48" cy="48" r="46" fill="none" stroke="#fff" stroke-width="2"/><path d="M38 30L66 48L38 66Z" fill="var(--red)"/></svg>
  <h1 class="hero-title abs">YOUR BUSINESS. YOUR LIFESTYLE. YOUR SUCCESS.</h1>
  <svg class="abs" style="left:950px;top:452px" width="50" height="50"><path d="M4 4C30 6 44 20 40 44M33 38l7 7 6-8" fill="none" stroke="#fff" stroke-width="1.5"/></svg>
</section>

<section>
  <div class="achieve abs"></div>
  <h2 class="section-title abs" style="top:673px">WHAT WE HELP OUR CLIENTS ACHIEVED</h2>
  <svg class="divider abs" style="top:725px" width="160" height="10"><path d="M0 5h66M94 5h66" stroke="var(--red)" stroke-width="1.5"/><circle cx="80" cy="5" r="3.5" fill="var(--red)"/></svg>

  <div class="goal abs" style="left:120px;top:783px">
    <div class="goal-icon"><svg width="36" height="36"><path d="M3 3v30h30" fill="none" stroke="#222" stroke-width="3"/><path d="M9 29v-9M15 29v-14M21 29v-11M27 29v-17" stroke="#222" stroke-width="4"/></svg></div>
    <div class="goal-title">Grow in size so your business<br>can get bigger</div>
    <div class="goal-text">Sed do eiusmod tempor incididunt ut labore et dolore magna aliqua. Ut enim ad minim veniam quis.</div>
  </div>
  <div class="goal active abs" style="left:450px;top:783px">
    <div class="goal-icon"><svg width="36" height="38"><rect x="6" y="3" width="22" height="30" rx="2" fill="none" stroke="var(--red)" stroke-width="3"/><path d="M11 10h12M11 17h4M18 17h5M11 23h4" stroke="var(--red)" stroke-width="2.5"/><circle cx="27" cy="28" r="7" fill="var(--red)"/><path d="M23.5 28l2.5 2.5 4.5-4.5" stroke="#fff" stroke-width="2" fill="none"/></svg></div>
    <div class="goal-title">Free up your time, so you can<br>live the lifestyle</div>
    <div class="goal-text">Sed do eiusmod tempor incididunt ut labore et dolore magna aliqua. Ut enim ad minim veniam quis.</div>
  </div>
  <div class="goal abs" style="left:780px;top:783px">
    <div class="goal-icon"><svg width="36" height="36"><path d="M5 32v-8M12 32v-12M19 32v-16M26 32v-20" stroke="#222" stroke-width="5"/><path d="M4 18L24 5M18 4h7v7" fill="none" stroke="#222" stroke-width="2.5"/></svg></div>
    <div class="goal-title">Increase in value, so you<br>maximise what your business</div>
    <div class="goal-text">Sed do eiusmod tempor incididunt ut labore et dolore magna aliqua. Ut enim ad minim veniam quis.</div>
  </div>
</section>

<form class="optin abs">
  <div class="optin-field abs" style="left:52px;width:157px">Enter your name</div>
  <div class="optin-field abs" style="left:223px;width:159px">Enter your surname</div>
  <div class="optin-field abs" style="left:395px;width:262px">Enter your email address</div>
  <div class="optin-btn abs">SIGN UP NOW</div>
</form>

<section>
  <h2 class="section-title abs" style="top:1116px">OUR SERVICES</h2>
  <svg class="divider abs" style="top:1161px" width="160" height="10"><path d="M0 5h66M94 5h66" stroke="var(--red)" stroke-width="1.5"/><circle cx="80" cy="5" r="3.5" fill="var(--red)"/></svg>

  <div class="service abs" style="left:140px;top:1216px">
    <svg class="service-icon" viewBox="0 0 34 28"><circle cx="7" cy="8" r="4" fill="var(--red)"/><circle cx="17" cy="8" r="4" fill="var(--red)"/><circle cx="27" cy="8" r="4" fill="var(--red)"/><path d="M1 20q6-8 12 0M11 20q6-8 12 0M21 20q6-8 12 0" fill="var(--red)"/></svg>
    <div><div class="service-name">PEOPLE</div><div class="service-text">Incididunt ut labore et dolore magna aliqua. Ut enim ad minim veniam, quis nostrud. Exercitation ullamco. <span class="more">READ MORE</span></div></div>
  </div>
  <div class="service abs" style="left:450px;top:1216px">
    <svg class="service-icon" viewBox="0 0 34 28"><path d="M4 10l12-7 14 12-12 8z" fill="none" stroke="var(--red)" stroke-width="2.5"/><path d="M9 14l12-7M12 18l12-7" stroke="var(--red)" stroke-width="2"/></svg>
    <div><div class="service-name">NEW EARNING STREAMS</div><div class="service-text">Exercitation ullamco laboris nisi ut aliquip ex ea commodo consequat. Duis aute irure dolor in reprehenderit in voluptate velit. <span class="more">READ MORE</span></div></div>
  </div>
  <div class="service abs" style="left:790px;top:1216px">
    <svg class="service-icon" viewBox="0 0 34 28"><path d="M2 8l8-4 7 5 7-5 8 4-6 10-9 6-9-6z" fill="var(--red)"/></svg>
    <div><div class="service-name">NEW BUSINESSES</div><div class="service-text">Duis aute irure dolor in reprehenderit in voluptate velitesse cillum dolore eu fugiat nulla pariatur. Excepteur sint occaecat. <span class="more">READ MORE</span></div></div>
  </div>
  <div class="service abs" style="left:140px;top:1368px">
    <svg class="service-icon" viewBox="0 0 34 28"><path d="M13 2h8l-2 5h-4z" fill="var(--red)"/><circle cx="17" cy="17" r="10" fill="var(--red)"/><text x="17" y="22" font-size="12" font-weight="700" fill="#fff" text-anchor="middle" font-family="Raleway,sans-serif">$</text></svg>
    <div><div class="service-name">FUNDING</div><div class="service-text">Laboris nisi ut aliquip ex ea commodo consequat. Duis aute irure dolor in reprehenderit in voluptate velit. <span class="more">READ MORE</span></div></div>
  </div>
  <div class="service abs" style="left:450px;top:1368px">
    <svg class="service-icon" viewBox="0 0 34 28"><circle cx="20" cy="6" r="5" fill="var(--red)"/><path d="M12 24q0-12 8-12t8 12z" fill="var(--red)"/><rect x="3" y="16" width="10" height="10" fill="var(--red)"/></svg>
    <div><div class="service-name">NEW MARKETS</div><div class="service-text">Esse cillum dolore eu fugiat nulla pariatur. Excepteur sint occaecat cupidatat non proident, sunt in culpa qui officia. <span class="more">READ MORE</span></div></div>
  </div>
  <div class="service abs" style="left:790px;top:1368px">
    <svg class="service-icon" viewBox="0 0 34 28"><rect x="3" y="8" width="28" height="18" rx="2" fill="var(--red)"/><path d="M12 8V4h10v4" fill="none" stroke="var(--red)" stroke-width="2.5"/><path d="M3 15h28" stroke="#fff" stroke-width="1.5"/></svg>
    <div><div class="service-name">BUSINESS SYSTEMS</div><div class="service-text">Cillum dolore eu fugiat nulla pariatur. Excepteur sint occaecatcupidatat non proident, sunt in culpa qui officia deserunt mollit. <span class="more">READ MORE</span></div></div>
  </div>
</section>

<section>
  <div class="why abs" role="img" aria-label="Dimmed photo of hands working over papers at a desk"></div>
  <h2 class="why-title abs">WHY WORK WITH US</h2>
  <svg class="divider abs" style="top:1632px" width="160" height="10"><path d="M0 5h66M94 5h66" stroke="#fff" stroke-width="1.5"/><circle cx="80" cy="5" r="3.5" fill="#fff"/></svg>
  <p class="why-text abs">Nostrud exercitation ullamco laboris nisi ut aliquip ex ea commodo consequat. Duis aute irure dolor in reprehenderit in voluptate velit esse cillum dolore eu fugiat.</p>
</section>

<section>
  <div class="team-tabs abs"><span class="on">All</span><span>|</span><span>Management</span><span>|</span><span>Technical</span></div>
  <h2 class="section-title abs" style="top:1878px">OUR TEAM</h2>
  <svg class="divider abs" style="top:1922px" width="160" height="10"><path d="M0 5h66M94 5h66" stroke="var(--red)" stroke-width="1.5"/><circle cx="80" cy="5" r="3.5" fill="var(--red)"/></svg>
  <span class="team-dot abs" style="left:984px"></span><span class="team-dot abs" style="left:1001px;background:var(--red)"></span><span class="team-dot abs" style="left:1018px"></span>

  <div class="member abs" style="left:0;top:1975px;background:#9a7a66" role="img" aria-label="Team member portrait"></div>
  <div class="member abs" style="left:200px;top:1975px;background:#6e4a3c" role="img" aria-label="Team member portrait"></div>
  <div class="member abs" style="left:400px;top:1975px;background:#55504c" role="img" aria-label="Team member portrait"></div>
  <div class="member abs" style="left:600px;top:1975px;background:#8d6a58" role="img" aria-label="Team member portrait"></div>
  <div class="member abs" style="left:800px;top:1975px;background:#8a5a48" role="img" aria-label="Team member portrait"></div>
  <div class="member abs" style="left:1000px;top:1975px;background:#b08a74" role="img" aria-label="Team member portrait"></div>
  <div class="member abs" style="left:0;top:2156px;background:#7c6a5c" role="img" aria-label="Team member portrait"></div>
  <div class="member abs" style="left:200px;top:2156px;background:#5e4438" role="img" aria-label="Team member portrait"></div>
  <div class="member abs" style="left:400px;top:2156px;background:#6a4634" role="img" aria-label="Team member portrait"></div>
  <div class="member abs" style="left:600px;top:2156px;background:#a2948a" role="img" aria-label="Team member portrait"></div>
  <div class="member abs" style="left:800px;top:2156px;background:#8e7262" role="img" aria-label="Team member portrait"></div>
  <div class="member abs" style="left:1000px;top:2156px;background:#4e3a30" role="img" aria-label="Team member portrait"></div>

  <div class="member-hover abs">
    <div class="member-name">Daniel Reyes</div>
    <div class="member-social"><span class="soc" aria-label="Social link"></span><span class="soc" aria-label="Social link"></span><span class="soc" aria-label="Social link"></span></div>
  </div>
</section>

<section>
  <svg class="abs" style="left:0;top:2403px" width="1200" height="366">
    <rect x="0" y="0" width="1200" height="366" fill="var(--black)"/>
    <path d="M0 0H630L680 322H0Z" fill="var(--red)"/>
    <path d="M0 322H1200V366H0Z" fill="#1a1a1a"/>
    <path d="M0 322H680V366H0Z" fill="#b02a24"/>
    <path d="M0 322H1200" stroke="rgba(255,255,255,.35)" stroke-width="1"/>
  </svg>

  <h2 class="quote-title abs" style="left:150px;top:2443px">WHAT OUR CUSTOMERS SAY</h2>
  <svg class="abs" style="left:150px;top:2495px" width="150" height="10"><path d="M0 5h62M86 5h62" stroke="#fff" stroke-width="1.5"/><circle cx="74" cy="5" r="3.5" fill="#fff"/></svg>
  <div class="avatar abs" role="img" aria-label="Customer portrait"></div>
  <div class="quote-mark abs" style="left:276px;top:2548px">“</div>
  <p class="quote-text abs">Enim ad minim veniam, quis nostrud exercitation ullamco laboris nisi ut aliquip ex ea commodo consequat. Duis aute irure dolor. <span style="font-size:22px">“</span></p>
  <span class="slide-dot abs" style="left:273px"></span><span class="slide-dot abs" style="left:297px"></span><span class="slide-dot abs" style="left:321px;background:#fff"></span><span class="slide-dot abs" style="left:345px"></span>

  <h2 class="quote-title abs" style="left:776px;top:2443px">CONTACT US</h2>
  <svg class="abs" style="left:776px;top:2495px" width="150" height="10"><path d="M0 5h62M86 5h62" stroke="#fff" stroke-width="1.5"/><circle cx="74" cy="5" r="3.5" fill="#fff"/></svg>
  <div class="contact-line abs" style="top:2530px"><svg width="14" height="22" style="flex:none;margin-top:4px"><path d="M7 20C2 13 1 10 1 7a6 6 0 0 1 12 0c0 3-1 6-6 13z" fill="none" stroke="#fff" stroke-width="2"/><circle cx="7" cy="7" r="2" fill="#fff"/></svg><span>52 Harlow Lane, Adelaide, SA,<br>5000, Australia</span></div>
  <div class="contact-line abs" style="top:2592px"><svg width="18" height="18" style="flex:none;margin-top:3px"><circle cx="9" cy="9" r="8" fill="none" stroke="#fff" stroke-width="1.8"/><path d="M6 5l2 2-1 2 2 2 2-1 2 2-2 2c-3 0-7-4-7-7z" fill="#fff"/></svg><span>08 5550 1847</span></div>
  <div class="contact-line abs" style="top:2646px"><svg width="16" height="12" style="flex:none;margin-top:6px"><rect width="16" height="12" fill="#fff"/><path d="M0 0l8 6 8-6" fill="none" stroke="var(--black)" stroke-width="1.5"/></svg><span>info@kestrelunion.com</span></div>

  <div class="footer-copy abs">©Kestrelunion2015.All Rights Reserved</div>
  <span class="footer-soc abs" style="left:792px" aria-label="Social link"></span>
  <span class="footer-soc abs" style="left:833px" aria-label="Social link"></span>
  <span class="footer-soc abs" style="left:873px" aria-label="Social link"></span>
</section>

</body>
</html>
```